Design a Website for an IT Support Company

We are an IT support company that provides commercial IT support and services to small and medium sized businesses. We are in need of a website to be developed for our business.
We would like to work with someone who is either familiar with the IT field, or has developed a website for an IT support company in the past.
Some examples of designs/layouts that we like:
https://www.veltragrid.example/
http://www.morvashelp.example/
http://kelbo.example/
http://www.nuvopathsystems.example/
http://www.quordesk.example/
I have attached a word document that gives a menu system/page layout format that we would like for our website as well as branch office phone numbers. Our logo is also attached that you can use for your design purposes. We currently do not have copy produced for all of the pages outlined in the word document, but would get this done during the project with the selected designer.
We would like the website to be SEO friendly & fully responsive. We would prefer a CMS format, however, we are open to HTML formats as well.

```html
<!DOCTYPE html>
<html lang="en">
<head>
<meta charset="utf-8">
<title>Kestrel IT — IT Support</title>
<link href="https://fonts.googleapis.com/css2?family=Raleway:wght@500;600;700;800&family=Open+Sans:wght@400;600;700&display=swap" rel="stylesheet">
<style>
:root{
  --blue:#0d6fb8;
  --blue-dark:#0a5a97;
  --ink:#1d1d1d;
  --text:#555;
  --muted:#777;
  --light:#f1f1f1;
  --footer:#262626;
  --footer-line:#3c3c3c;
  --white:#fff;
}
*{box-sizing:border-box;margin:0;padding:0}
html,body{width:1200px;height:3742px;overflow:hidden}
body{font-family:"Open Sans",sans-serif;color:var(--text);background:var(--white);position:relative}
.section{position:absolute;left:0;width:1200px}
.wrap{position:absolute;left:90px;width:1020px;top:0}
.sec-title{font-family:"Raleway",sans-serif;font-weight:800;font-size:31px;color:var(--blue);text-align:center;letter-spacing:1px;position:absolute;left:0;width:1200px}
.sec-lead{position:absolute;left:270px;width:660px;text-align:center;font-size:14px;line-height:24px;color:var(--muted)}
.icon-box{width:40px;height:40px;background:var(--blue);display:flex;align-items:center;justify-content:center}
.icon-box svg{width:20px;height:20px;fill:none;stroke:#fff;stroke-width:2;stroke-linecap:round;stroke-linejoin:round}

/* top bar */
.topbar{top:0;height:30px;background:var(--blue);color:#fff;font-size:12px;font-weight:600}
.topbar .call{position:absolute;left:92px;top:7px;display:flex;align-items:center;gap:6px}
.topbar .login{position:absolute;left:840px;top:7px;display:flex;gap:6px;align-items:center}
.topbar .social{position:absolute;left:968px;top:0;display:flex}
.topbar .social span{width:36px;height:30px;border-left:1px solid rgba(255,255,255,.35);display:flex;align-items:center;justify-content:center}
.topbar .social i{width:10px;height:10px;background:#fff;border-radius:50%;display:block}

/* header */
.header{top:30px;height:112px;background:#fff}
.brand{position:absolute;left:90px;top:32px;display:flex;align-items:center;gap:10px}
.brand .dot{width:30px;height:30px;border-radius:50%;background:var(--blue)}
.brand .name{font-family:"Raleway",sans-serif;font-weight:700;font-size:32px;color:var(--ink)}
.nav{position:absolute;left:400px;top:47px;display:flex;gap:40px;font-family:"Raleway",sans-serif;font-weight:600;font-size:15px;color:var(--ink)}
.quote{position:absolute;left:927px;top:36px;height:42px;display:flex}
.quote .sq{width:42px;background:var(--ink);display:flex;align-items:center;justify-content:center}
.quote .sq i{width:12px;height:12px;border-radius:50%;background:#fff;display:block}
.quote .lbl{width:128px;background:var(--blue);color:#fff;font-size:12px;font-weight:700;display:flex;align-items:center;justify-content:center}

/* hero */
.hero{top:142px;height:524px;background:linear-gradient(100deg,#0c1a2a 0%,#1f4a6e 35%,#3b6c8f 55%,#1b2a3a 80%,#0f1820 100%)}
.hero h1{position:absolute;left:90px;top:195px;font-family:"Raleway",sans-serif;font-weight:700;font-size:36px;color:#fff;letter-spacing:1px}
.hero h2{position:absolute;left:90px;top:242px;font-family:"Raleway",sans-serif;font-weight:600;font-size:22px;color:#fff;letter-spacing:2px}
.hero .btn{position:absolute;top:292px;height:44px;display:flex;align-items:center;justify-content:center;color:#fff;font-size:14px;font-weight:700;letter-spacing:1px}
.btn-dark{left:90px;width:170px;background:#1c1c1c}
.btn-blue{left:272px;width:172px;background:var(--blue)}

/* about */
.about{top:666px;height:514px;background:#fff}
.about .photo{position:absolute;left:117px;top:172px;width:472px;height:262px;background:linear-gradient(180deg,#e8eef3,#9aa8b5 60%,#5a6674)}
.about .copy{position:absolute;left:618px;top:170px;width:470px}
.about h4{font-family:"Raleway",sans-serif;font-weight:700;font-size:13px;color:var(--ink);margin-bottom:22px}
.about p{font-size:11.5px;line-height:21px;margin-bottom:14px}
.about ul{list-style:none;margin-top:10px}
.about li{display:flex;align-items:center;gap:12px;font-size:11.5px;margin-bottom:17px}
.about li b{width:13px;height:13px;background:var(--blue);display:flex;align-items:center;justify-content:center}

/* services */
.services{top:1180px;height:641px;background:var(--light)}
.svc{position:absolute;width:320px;text-align:center}
.svc .icon-box{margin:0 auto 12px}
.svc h3{font-family:"Raleway",sans-serif;font-weight:700;font-size:15px;color:var(--ink);letter-spacing:1px;margin-bottom:8px}
.svc p{font-size:12px;line-height:24px}

/* why */
.why{top:1821px;height:594px;background:#fff}
.why-item{position:absolute;width:300px;text-align:center}
.why-item .icon-box{margin:0 auto 14px}
.why-item h3{font-family:"Raleway",sans-serif;font-weight:700;font-size:13px;color:var(--ink);margin-bottom:8px}
.why-item p{font-size:11.5px;line-height:22px}
.why .person{position:absolute;left:668px;top:175px;width:430px;height:419px;background:linear-gradient(180deg,#f4f4f4,#e2e2e6 40%,#5b6b8e 75%,#465679)}

/* stats */
.stats{top:2415px;height:222px;background:var(--blue)}
.stat{position:absolute;width:200px;text-align:center;color:#fff;top:42px}
.stat .ico{width:44px;height:44px;background:#fff;margin:0 auto;display:flex;align-items:center;justify-content:center}
.stat .ico svg{width:22px;height:22px;fill:none;stroke:var(--blue);stroke-width:2.2;stroke-linecap:round;stroke-linejoin:round}
.stat .num{font-family:"Raleway",sans-serif;font-weight:800;font-size:33px;margin-top:14px}
.stat .lbl{font-size:10px;font-weight:700;margin-top:6px;letter-spacing:.5px}

/* projects */
.projects{top:2637px;height:676px;background:#fff}
.tile{position:absolute;width:225px;height:202px;background:linear-gradient(135deg,#3a3a3a,#1b1b1b)}
.tile .art{position:absolute;left:0;top:0;width:225px;height:168px}
.tile .cap{position:absolute;left:0;bottom:0;width:225px;height:34px;background:var(--blue);color:#fff;font-size:11px;font-weight:700;display:flex;align-items:center;justify-content:center}

/* newsletter */
.newsletter{top:3313px;height:120px;background:var(--blue)}
.newsletter h3{position:absolute;left:120px;top:42px;font-family:"Raleway",sans-serif;font-weight:700;font-size:24px;color:#fff}
.newsletter .field{position:absolute;left:484px;top:38px;width:404px;height:47px;background:#fff;font-size:12px;color:#888;padding:16px 16px}
.newsletter .go{position:absolute;left:896px;top:38px;width:167px;height:47px;background:#1c1c1c;color:#fff;font-size:12px;font-weight:700;display:flex;align-items:center;justify-content:center}

/* footer */
.footer{top:3433px;height:309px;background:var(--footer);color:#fff}
.footer .brand{top:45px;left:92px}
.footer .brand .name{color:#fff;font-size:28px}
.footer .about-txt{position:absolute;left:90px;top:105px;width:330px;font-size:13px;line-height:19px;text-align:justify;color:#fff}
.footer h4{position:absolute;font-family:"Raleway",sans-serif;font-weight:700;font-size:18px;letter-spacing:1px}
.footer .contact{position:absolute;left:462px;top:105px;font-size:11.5px;line-height:26px;width:220px}
.footer .contact b{font-weight:700}
.footer .vline{position:absolute;left:760px;top:45px;width:1px;height:170px;background:var(--footer-line)}
.footer .soc{position:absolute;left:794px;top:113px;display:flex;gap:8px}
.footer .soc span{width:26px;height:26px;border-radius:50%;background:#444;display:flex;align-items:center;justify-content:center}
.footer .soc i{width:8px;height:8px;background:#bbb;border-radius:50%;display:block}
.footer .bar{position:absolute;left:90px;top:240px;width:1020px;height:1px;background:var(--footer-line)}
.footer .copy{position:absolute;left:90px;top:260px;font-size:12px}
.footer .fnav{position:absolute;left:728px;top:260px;display:flex;gap:40px;font-size:12px}
</style>
</head>
<body>

<div class="section topbar">
  <div class="call">
    <svg width="10" height="14" viewBox="0 0 10 14"><rect x="1" y="1" width="8" height="12" rx="1.5" fill="none" stroke="#fff" stroke-width="1.5"/></svg>
    Call Us Today: 555-014-2290
  </div>
  <div class="login">
    <svg width="10" height="11" viewBox="0 0 10 11"><rect x="1" y="5" width="8" height="6" fill="#fff"/><path d="M3 5V3a2 2 0 0 1 4 0v2" fill="none" stroke="#fff" stroke-width="1.4"/></svg>
    Login / Register
  </div>
  <div class="social"><span><i></i></span><span><i></i></span><span><i></i></span></div>
</div>

<div class="section header">
  <div class="brand"><div class="dot"></div><div class="name">Kestrel IT</div></div>
  <nav class="nav"><span>Home</span><span>Services ˅</span><span>Why Kestrel IT</span><span>Contact</span></nav>
  <div class="quote"><div class="sq"><i></i></div><div class="lbl">GET A QUOTE</div></div>
</div>

<div class="section hero" role="img" aria-label="Server room background with a businessman holding a tablet showing cloud network icons">
  <h1>FAST ONSITE IT SUPPORT</h1>
  <h2>ANYWHERE IN THE WORLD</h2>
  <div class="btn btn-dark">LEARN MORE</div>
  <div class="btn btn-blue">CONTACT US</div>
</div>

<div class="section about">
  <h2 class="sec-title" style="top:55px">ABOUT US</h2>
  <p class="sec-lead" style="top:102px">Lorem ipsum dolor sit amet, pellentesque enim lorem quis vivamus amet. lectus nullam sint. risus quis accumsan duis lacinia. quam eleifend ut amet pede.</p>
  <div class="photo" role="img" aria-label="Team of business people joining hands"></div>
  <div class="copy">
    <h4>WE ARE CREATE WEB DEVELOPMENT AGENCY</h4>
    <p>Lorem ipsum dolor sit amet, ligula magna at etiam aliquip venenatis. Vitae sit felis donec, suscipit tortor et sapien donec ac nec. Nam vel eu amet, nisl imperdiet nec ad morbi, sodales ipsum, consequat purus vitae integer maecenas.</p>
    <p>Lorem ipsum dolor sit amet, ligula magna at etiam aliquip venenatis. Vitae sit felis donec, suscipit tortor et sapien donec ac nec. Nam vel eu amet.</p>
    <ul>
      <li><b><svg width="9" height="9" viewBox="0 0 9 9"><path d="M1.5 4.5l2 2 4-4" fill="none" stroke="#fff" stroke-width="1.5"/></svg></b>100% Secure Service</li>
      <li><b><svg width="9" height="9" viewBox="0 0 9 9"><path d="M1.5 4.5l2 2 4-4" fill="none" stroke="#fff" stroke-width="1.5"/></svg></b>24/7 Support</li>
      <li><b><svg width="9" height="9" viewBox="0 0 9 9"><path d="M1.5 4.5l2 2 4-4" fill="none" stroke="#fff" stroke-width="1.5"/></svg></b>100% Client satisfy</li>
    </ul>
  </div>
</div>

<div class="section services">
  <h2 class="sec-title" style="top:55px">OUR SERVICE</h2>
  <p class="sec-lead" style="top:102px">Lorem ipsum dolor sit amet, pellentesque enim lorem quis vivamus amet. lectus nullam sint. risus quis accumsan duis lacinia. quam eleifend ut amet pede.</p>

  <div class="svc" style="left:107px;top:190px"><div class="icon-box"><svg viewBox="0 0 20 20"><circle cx="10" cy="10" r="7"/><path d="M3 10h14M10 3c3 3 3 11 0 14M10 3c-3 3-3 11 0 14"/></svg></div><h3>WEB DEVELOPMENT</h3><p>Lorem ipsum dolor sit amet, ligula magna at etiam aliquip venenatis. Vitae sit felis donec, suscipit tortor et sapien donec ac nec. Nam vel eu amet</p></div>
  <div class="svc" style="left:436px;top:190px"><div class="icon-box"><svg viewBox="0 0 20 20"><rect x="6" y="2" width="8" height="16" rx="1.5"/><path d="M9 15h2"/></svg></div><h3>APPS DEVELOPMENT</h3><p>Lorem ipsum dolor sit amet, ligula magna at etiam aliquip venenatis. Vitae sit felis donec, suscipit tortor et sapien donec ac nec. Nam vel eu amet</p></div>
  <div class="svc" style="left:768px;top:190px"><div class="icon-box"><svg viewBox="0 0 20 20"><path d="M4 16l1-4 8-8 3 3-8 8z"/></svg></div><h3>GRAPHIC DESIGN</h3><p>Lorem ipsum dolor sit amet, ligula magna at etiam aliquip venenatis. Vitae sit felis donec, suscipit tortor et sapien donec ac nec. Nam vel eu amet</p></div>

  <div class="svc" style="left:107px;top:413px"><div class="icon-box"><svg viewBox="0 0 20 20"><path d="M3 17h14M5 14V6M9 14V3M13 14V8"/></svg></div><h3>SOFTWARE DEVELOPMENT</h3><p>Lorem ipsum dolor sit amet, ligula magna at etiam aliquip venenatis. Vitae sit felis donec, suscipit tortor et sapien donec ac nec. Nam vel eu amet</p></div>
  <div class="svc" style="left:436px;top:413px"><div class="icon-box"><svg viewBox="0 0 20 20"><rect x="2" y="6" width="16" height="11" rx="1.5"/><path d="M7 6l1.5-2h3L13 6"/><circle cx="10" cy="11.5" r="3"/></svg></div><h3>PHOTOGRAPHY</h3><p>Lorem ipsum dolor sit amet, ligula magna at etiam aliquip venenatis. Vitae sit felis donec, suscipit tortor et sapien donec ac nec. Nam vel eu amet</p></div>
  <div class="svc" style="left:768px;top:413px"><div class="icon-box"><svg viewBox="0 0 20 20"><rect x="3" y="3" width="14" height="14" rx="1"/><path d="M3 7h14M7 7v10"/></svg></div><h3>CMS THEME</h3><p>Lorem ipsum dolor sit amet, ligula magna at etiam aliquip venenatis. Vitae sit felis donec, suscipit tortor et sapien donec ac nec. Nam vel eu amet</p></div>
</div>

<div class="section why">
  <h2 class="sec-title" style="top:58px">WHY CHOOSE US</h2>
  <p class="sec-lead" style="top:105px">Lorem ipsum dolor sit amet, pellentesque enim lorem quis vivamus amet. lectus nullam sint. risus quis accumsan duis lacinia. quam eleifend ut amet pede.</p>

  <div class="why-item" style="left:95px;top:195px"><div class="icon-box"><svg viewBox="0 0 20 20"><path d="M7 6l-4 4 4 4M13 6l4 4-4 4"/></svg></div><h3>CLEAN CODE</h3><p>Lorem ipsum dolor sit amet, ligula magna at etiam aliquip venenatis. Vitae sit felis donec, suscipit tortor et sapien donec ac nec.</p></div>
  <div class="why-item" style="left:419px;top:195px"><div class="icon-box"><svg viewBox="0 0 20 20"><path d="M5 3h3l1.5 4-2 1.5a9 9 0 0 0 4 4l1.5-2 4 1.5v3a1.5 1.5 0 0 1-1.5 1.5A13 13 0 0 1 3.5 4.5 1.5 1.5 0 0 1 5 3z"/></svg></div><h3>24/7 SUPPORT</h3><p>Lorem ipsum dolor sit amet, ligula magna at etiam aliquip venenatis. Vitae sit felis donec, suscipit tortor et sapien donec ac nec.</p></div>
  <div class="why-item" style="left:95px;top:394px"><div class="icon-box"><svg viewBox="0 0 20 20"><path d="M4 16l1-4 8-8 3 3-8 8z"/></svg></div><h3>MODERN DESIGN</h3><p>Lorem ipsum dolor sit amet, ligula magna at etiam aliquip venenatis. Vitae sit felis donec, suscipit tortor et sapien donec ac nec.</p></div>
  <div class="why-item" style="left:419px;top:394px"><div class="icon-box"><svg viewBox="0 0 20 20"><rect x="6" y="2" width="8" height="16" rx="1.5"/><path d="M9 15h2"/></svg></div><h3>MOBILE RESPONSIVE</h3><p>Lorem ipsum dolor sit amet, ligula magna at etiam aliquip venenatis. Vitae sit felis donec, suscipit tortor et sapien donec ac nec.</p></div>

  <div class="person" role="img" aria-label="Smiling woman in a blue sweater giving a thumbs up"></div>
</div>

<div class="section stats">
  <div class="stat" style="left:117px"><div class="ico"><svg viewBox="0 0 22 22"><circle cx="11" cy="11" r="8"/><path d="M3 11h16M11 3c3.5 3.5 3.5 12.5 0 16M11 3c-3.5 3.5-3.5 12.5 0 16"/></svg></div><div class="num">150</div><div class="lbl">WEBSITE CREATED</div></div>
  <div class="stat" style="left:367px"><div class="ico"><svg viewBox="0 0 22 22"><circle cx="11" cy="7" r="3"/><path d="M5 18a6 6 0 0 1 12 0"/><circle cx="4.5" cy="9" r="2"/><circle cx="17.5" cy="9" r="2"/></svg></div><div class="num">250</div><div class="lbl">HAPPY CLIENT</div></div>
  <div class="stat" style="left:618px"><div class="ico"><svg viewBox="0 0 22 22"><path d="M4 18l1-4 9-9 3 3-9 9z"/></svg></div><div class="num">24</div><div class="lbl">DEVELOPER</div></div>
  <div class="stat" style="left:870px"><div class="ico"><svg viewBox="0 0 22 22"><path d="M5 6h12M5 11h12M5 16h12"/></svg></div><div class="num">260</div><div class="lbl">AWARDS WIN</div></div>
</div>

<div class="section projects">
  <h2 class="sec-title" style="top:55px">OUR PROJECT</h2>
  <p class="sec-lead" style="top:102px">Lorem ipsum dolor sit amet, pellentesque enim lorem quis vivamus amet. lectus nullam sint. risus quis accumsan duis lacinia. quam eleifend ut amet pede.</p>

  <div class="tile" style="left:102px;top:182px"><div class="art" role="img" aria-label="Red hardcover book mockup" style="background:linear-gradient(135deg,#2a2a2a,#7a1d1d 60%,#2a2a2a)"></div><div class="cap">BOOK COVER</div></div>
  <div class="tile" style="left:354px;top:182px"><div class="art" role="img" aria-label="Orange printed brochure mockup" style="background:linear-gradient(135deg,#555,#c8452c 55%,#333)"></div><div class="cap">GRAPHIC DESIGN</div></div>
  <div class="tile" style="left:606px;top:182px"><div class="art" role="img" aria-label="Flyer layouts in blue and white" style="background:linear-gradient(135deg,#f2f2f2,#9ecbe0 50%,#e8e8e8)"></div><div class="cap">WEB DEVELOPMENT</div></div>
  <div class="tile" style="left:856px;top:182px"><div class="art" role="img" aria-label="Printed template sheets on grey" style="background:linear-gradient(135deg,#8a8a8a,#e4e4e4 50%,#6c6c6c)"></div><div class="cap">PSD TEMPLATE</div></div>

  <div class="tile" style="left:102px;top:412px"><div class="art" role="img" aria-label="Mobile app screens mockup" style="background:linear-gradient(135deg,#1d2b30,#3c7c84 50%,#1a2226)"></div><div class="cap">APPS DESIGN</div></div>
  <div class="tile" style="left:354px;top:412px"><div class="art" role="img" aria-label="Business cards in blue and black" style="background:linear-gradient(135deg,#1a1a1a,#2f8fcf 55%,#1a1a1a)"></div><div class="cap">CARD DESIGN</div></div>
  <div class="tile" style="left:606px;top:412px"><div class="art" role="img" aria-label="Orange and white business cards" style="background:linear-gradient(135deg,#1a1a1a,#e25d2a 45%,#eee 70%,#1a1a1a)"></div><div class="cap">CREATIVE DESIGN</div></div>
  <div class="tile" style="left:856px;top:412px"><div class="art" role="img" aria-label="Blue and white stationery cards" style="background:linear-gradient(135deg,#111,#e9eef2 45%,#2d8ad0 70%,#111)"></div><div class="cap">BOOK COVER</div></div>
</div>

<div class="section newsletter">
  <h3>Subscribe to our newsletter</h3>
  <div class="field">Email Address</div>
  <div class="go">SUBSCRIBE</div>
</div>

<div class="section footer">
  <div class="brand"><div class="dot"></div><div class="name">Kestrel IT</div></div>
  <p class="about-txt">Lorem ipsum dolor sit amet, consectetur adipisicing elit, sed do eiusmod tempor incididunt ut labore et dolore.Lorem ipsum dolor sit amet, consectetur adipisicing elit, sed do eiusmod tempor incididunt ut labore et</p>
  <h4 style="left:462px;top:55px">CONTACT US</h4>
  <div class="contact">
    <div><b>Address:</b> 48 Harbor Row, Suite 6,<br>&nbsp;&nbsp;&nbsp;&nbsp;&nbsp;&nbsp;&nbsp;&nbsp;&nbsp;&nbsp;&nbsp;&nbsp;&nbsp;&nbsp;&nbsp;Fenwick 20417</div>
    <div><b>Email:</b> info@kestrelit.example</div>
    <div><b>Phone:</b> 555-014-7731</div>
  </div>
  <div class="vline"></div>
  <h4 style="left:796px;top:55px">FOLLOW US</h4>
  <div class="soc"><span><i></i></span><span><i></i></span><span><i></i></span><span><i></i></span><span><i></i></span></div>
  <div class="bar"></div>
  <div class="copy">© 2017 Kestrel IT. All rights reserved.</div>
  <div class="fnav"><span>Home</span><span>Services</span><span>Why Kestrel IT</span><span>Contact</span></div>
</div>

</body>
</html>
```